TRESSLY FACEBOOK DESIGN

I need new design for facebook https://www.facebook.com/tresslyitalia.
Our Businnes is Hair care , hair replacement , hair transplant . hair regrowth . i NEED MEDICAL AND PROFESSIONAL DESIGN. I NEED ALSO RESPONSIVE DESIGN

Target Market(s)

Consumers

Industry/Entity Type

MEDICAL AND COSMETICS

Colors
0054AA
0677BA
7BADD7
CADEEF
E8F1F8

Requirements
Must have
• MEDICAL
Nice to have
• RESPONSIVE DESIGN

```html
<!DOCTYPE html>
<html lang="it">
<head>
<meta charset="UTF-8">
<title>Tressly – Facebook Cover</title>
<link href="https://fonts.googleapis.com/css2?family=Montserrat:wght@500;600;700&display=swap" rel="stylesheet">
<style>
  :root {
    --brand-deep: #0054AA;
    --brand-mid: #0677BA;
    --brand-bright: #2A9FDB;
    --brand-soft: #7BADD7;
    --brand-pale: #CADEEF;
    --brand-mist: #E8F1F8;
    --page-bg: #EEF3F8;
    --white: #FFFFFF;
  }
  * { box-sizing: border-box; margin: 0; padding: 0; }
  html, body { width: 1200px; height: 1200px; overflow: hidden; }
  body {
    background: var(--page-bg);
    font-family: "Montserrat", Arial, sans-serif;
    position: relative;
  }
  .cover {
    position: absolute;
    left: 118px;
    top: 346px;
    width: 965px;
    height: 508px;
    background: var(--white);
    overflow: hidden;
    box-shadow: 0 20px 40px rgba(0, 60, 110, 0.18);
  }
  .cover-shapes {
    position: absolute;
    inset: 0;
    width: 965px;
    height: 508px;
  }
  .brand {
    position: absolute;
    left: 55px;
    top: 100px;
  }
  .brand-name {
    display: flex;
    align-items: center;
    gap: 12px;
    font-size: 48px;
    font-weight: 700;
    color: var(--brand-deep);
    letter-spacing: -0.5px;
    line-height: 1;
  }
  .brand-dot {
    width: 40px;
    height: 40px;
    border-radius: 50%;
    background: var(--brand-bright);
  }
  .brand-tagline {
    margin-top: 14px;
    font-size: 13px;
    font-weight: 500;
    color: var(--brand-deep);
    letter-spacing: 0.2px;
  }
  .headline {
    position: absolute;
    left: 50px;
    top: 254px;
    font-size: 46px;
    font-weight: 600;
    line-height: 50px;
    color: var(--brand-bright);
    letter-spacing: -0.5px;
  }
  .lead {
    position: absolute;
    left: 51px;
    top: 416px;
    width: 380px;
    font-size: 11px;
    font-weight: 600;
    line-height: 19px;
    color: var(--brand-deep);
  }
</style>
</head>
<body>
  <section class="cover">
    <svg class="cover-shapes" viewBox="0 0 965 508" xmlns="http://www.w3.org/2000/svg">
      <defs>
        <linearGradient id="portraitTone" x1="0" y1="0" x2="1" y2="1">
          <stop offset="0" stop-color="#F4EDE4"/>
          <stop offset="0.5" stop-color="#D9D2CC"/>
          <stop offset="1" stop-color="#B8BCC4"/>
        </linearGradient>
      </defs>

      <!-- corner ring, top left -->
      <circle cx="25" cy="-30" r="83" fill="none" stroke="var(--brand-mid)" stroke-width="38"/>

      <!-- portrait area -->
      <rect x="440" y="60" width="470" height="448" rx="40" fill="url(#portraitTone)"
            role="img" aria-label="Foto di una donna sorridente e di un uomo in giacca grigia, in piedi schiena contro schiena"/>

      <!-- soft bottom wave band -->
      <path d="M0 472 C 200 462, 380 452, 560 456 C 720 460, 860 466, 965 470 L965 508 L0 508 Z"
            fill="var(--brand-pale)" opacity="0.75"/>

      <!-- ring, bottom right -->
      <circle cx="892" cy="432" r="80" fill="none" stroke="var(--brand-mid)" stroke-width="52"/>
    </svg>

    <div class="brand">
      <div class="brand-name"><span class="brand-dot"></span>Tressly</div>
      <div class="brand-tagline">CURA E REINTEGRAZIONE DEI CAPELLI</div>
    </div>

    <h1 class="headline">Ci prendiamo<br>cura dei tuoi<br>capelli</h1>

    <p class="lead">Lorem ipsum dolor sit amet, consectetur adipiscing elit, sed do eiusmod tempor.</p>
  </section>
</body>
</html>
```